Eye Catching Email Marketing design

Our health care consulting firm is based in New York City. We sell health care consulting Services to medical practices (doctors). We need a powerful email marketing design to use as one of our primary selling tools to attract new clients. The Design should convey health care knowledge, expertise professionalism, cutting edge technology and the services we offer. <br/>The design should incorporate our logo and its colors (blue and white) but we want it to be eye catching and vibrant, so other colors be included. We are open to the designer's creativity. Any pictures used should show diversity (races)and should include women. Designers can find our logo and other graphics on our website at www harbor crest advisory.com. Please feel free to ask questions.<br/><br/>

Target Market(s)

Health care professionals, executives and Doctors.

Colors

Designer to choose colors to be used in the design.

Requirements
Nice to have
• What ever the design feels will help make this design vibrant

```html
<!DOCTYPE html>
<html lang="en">
<head>
<meta charset="utf-8">
<title>Harbor Crest Advisory – Email</title>
<link href="https://fonts.googleapis.com/css2?family=Montserrat:wght@400;500;600;700&display=swap" rel="stylesheet">
<style>
:root{
  --green:#8ad43a;
  --sky:#33a6d8;
  --navy:#0a55a8;
  --ink:#1a4f9c;
  --white:#ffffff;
  --page:#ffffff;
}
*{box-sizing:border-box;margin:0;padding:0}
html,body{width:1200px;height:4258px;overflow:hidden;background:var(--page)}
body{font-family:'Montserrat',sans-serif;color:var(--ink);position:relative}
.col{position:absolute;left:170px;width:842px}
.topbar{top:0;height:44px;background:var(--green);display:flex;justify-content:space-around;align-items:center;color:var(--white);font-size:13px}
.topbar span{display:flex;align-items:center;gap:6px}
.hero{position:absolute;top:44px;left:144px;width:894px;height:414px;background:linear-gradient(135deg,#3d4a52,#9aa7ae 45%,#5b646a 70%,#b8c1c6)}
.brand-box{position:absolute;top:0;left:588px;width:280px;height:316px;background:var(--white);padding:34px 16px 0}
.brand-name{font-size:22px;font-weight:600;color:var(--navy);text-align:center;line-height:1.2}
.brand-sub{font-size:11px;color:var(--ink);text-align:center;margin-top:8px;letter-spacing:.5px}
.brand-tag{margin-top:60px;font-size:32px;line-height:1.13;color:var(--green);font-weight:500}
.btn{display:inline-block;background:var(--white);color:var(--ink);font-size:17px;padding:18px 28px;border:none}
.btn-green{background:var(--green);color:var(--white)}
.help{top:458px;height:298px;background:var(--sky);text-align:center;color:var(--white);padding-top:20px}
.help h2{font-size:30px;font-weight:500;letter-spacing:.5px}
.rule{height:2px;background:var(--white);margin:22px auto}
.help p{font-size:16px;line-height:1.75;width:720px;margin:0 auto 28px}
.split{display:flex;height:100%}
.split > div{width:421px;height:100%}
.photo{position:relative}
.welcome{top:756px;height:512px}
.welcome .copy{padding:80px 28px 0 14px}
.welcome h3{font-size:40px;font-weight:500;color:var(--sky)}
.welcome h4{font-size:40px;font-weight:500;color:var(--green);line-height:1.1;margin-top:12px}
.welcome p{font-size:17px;line-height:1.65;margin:22px 0 32px}
.feature{top:1268px;height:439px}
.feature .copy{background:var(--green);color:var(--white);padding:80px 30px 0}
.feature h3{font-size:33px;font-weight:600}
.feature p{font-size:17px;line-height:1.65;margin:22px 0 30px}
.checks{top:1707px;height:512px}
.checks .copy{background:var(--sky);color:var(--white);text-align:center;padding-top:60px}
.checks h3{font-size:33px;font-weight:600}
.checks ul{list-style:none;text-align:left;width:290px;margin:28px auto 30px}
.checks li{font-size:17px;height:37px;display:flex;align-items:center;gap:8px}
.services{top:2219px;height:402px;background:var(--navy);color:var(--white);text-align:center;padding-top:48px}
.services h3{font-size:33px;font-weight:600}
.services p{font-size:17px;line-height:1.65;width:760px;margin:26px auto 0}
.services .rule{width:450px;margin:28px auto 20px}
.icons{display:flex;justify-content:space-around;padding:0 6px}
.icon{width:200px}
.icon svg{width:80px;height:80px}
.icon div{font-size:17px;font-weight:700;line-height:1.15;margin-top:20px;letter-spacing:-.5px}
.cards{top:2621px;height:407px;background:var(--green);display:flex;justify-content:space-between;padding:20px 14px 0}
.card{width:254px;text-align:center;color:var(--white)}
.card .img{height:202px}
.card p{font-size:16px;line-height:1.3;margin:38px 0 26px}
.card .btn{padding:18px 26px}
.lab{top:3028px;height:484px}
.lab .copy{padding:84px 30px 0 14px}
.lab h3{font-size:33px;font-weight:600;color:var(--green)}
.lab p{font-size:17px;line-height:1.65;margin-top:64px;padding-left:12px}
.ceo{top:3512px;height:537px}
.ceo .copy{padding:66px 30px 0 40px}
.ceo h3{font-size:33px;font-weight:600;color:var(--green)}
.ceo p{font-size:17px;line-height:1.95;margin-top:18px}
.ceo .regards{font-size:17px;margin-top:38px}
.signature{width:260px;height:110px;margin-top:14px;background:linear-gradient(90deg,#eef2f7,#ffffff)}
.ceo .title{font-size:17px;font-weight:600;color:var(--green);margin-top:14px;letter-spacing:-.5px}
.footer{top:4049px;height:151px;background:var(--navy);color:var(--white);text-align:center;padding-top:28px}
.social{display:flex;justify-content:center;gap:28px}
.social span{width:42px;height:42px;border:2px solid var(--white);border-radius:50%}
.footer .links{font-size:14px;margin-top:34px}
</style>
</head>
<body>

<div class="col topbar">
  <span>✎ Your Address</span>
  <span>✉ info@example.com</span>
  <span>▤ www.example.com</span>
  <span>☎ +1 234 56789</span>
</div>

<div class="hero" role="img" aria-label="Photo of a diverse medical team meeting around a conference table">
  <div class="brand-box">
    <div class="brand-name">Harbor Crest</div>
    <div class="brand-sub">Harbor Crest Advisory LLC</div>
    <div class="brand-tag">ADVANCING HEALTHCARE OPERATIONS</div>
  </div>
</div>

<section class="col help">
  <h2>How Can We Help You?</h2>
  <div class="rule" style="width:496px"></div>
  <p>Lorem ipsum dolor sit amet, consectetur adipiscing elit, sed do eiusmod tempor incididunt ut labore et dolore magna aliqua.</p>
  <a class="btn">Read More</a>
</section>

<section class="col welcome">
  <div class="split">
    <div class="photo" role="img" aria-label="Photo of smiling female doctor holding a tablet with two colleagues" style="background:linear-gradient(160deg,#d9dde0,#f4f4f2 40%,#2d2f33 75%,#e8e9ea)"></div>
    <div class="copy">
      <h3>Welcome</h3>
      <h4>Harbor Crest Advisory</h4>
      <p>Lorem ipsum dolor sit amet, consectetur adipiscing elit, sed do eiusmod tempor incididunt ut labore et dolore magna.</p>
      <a class="btn btn-green">Read More</a>
    </div>
  </div>
</section>

<section class="col feature">
  <div class="split">
    <div class="copy">
      <h3>Lorem Ipsum</h3>
      <p>Lorem ipsum dolor sit amet, consectetur adipiscing elit, sed do eiusmod tempor incididunt ut labore et dolore magna.</p>
      <div style="text-align:center"><a class="btn" style="color:var(--green)">Read More</a></div>
    </div>
    <div class="photo" role="img" aria-label="Photo of a bright hospital corridor with staff" style="background:linear-gradient(180deg,#eef2f4,#c9d3d8 50%,#e6ecee)"></div>
  </div>
</section>

<section class="col checks">
  <div class="split">
    <div class="photo" role="img" aria-label="Photo of smiling nurse in scrubs and cap with stethoscope" style="background:linear-gradient(180deg,#ffffff 20%,#c9cfe6 55%,#7f8fd6)"></div>
    <div class="copy">
      <h3>Lorem Ipsum</h3>
      <ul>
        <li><svg width="18" height="16" viewBox="0 0 18 16"><path d="M2 9l5 5L16 2" fill="none" stroke="#1b2a3a" stroke-width="3"/></svg>Lorem ipsum dolor sit amet</li>
        <li><svg width="18" height="16" viewBox="0 0 18 16"><path d="M2 9l5 5L16 2" fill="none" stroke="#1b2a3a" stroke-width="3"/></svg>Lorem ipsum dolor sit amet</li>
        <li><svg width="18" height="16" viewBox="0 0 18 16"><path d="M2 9l5 5L16 2" fill="none" stroke="#1b2a3a" stroke-width="3"/></svg>Lorem ipsum dolor sit amet</li>
        <li><svg width="18" height="16" viewBox="0 0 18 16"><path d="M2 9l5 5L16 2" fill="none" stroke="#1b2a3a" stroke-width="3"/></svg>Lorem ipsum dolor sit amet</li>
      </ul>
      <a class="btn" style="color:var(--sky)">Read More</a>
    </div>
  </div>
</section>

<section class="col services">
  <h3>Lorem Ipsum</h3>
  <p>Lorem ipsum dolor sit amet, consectetur adipiscing elit, sed do eiusmod tempor incididunt ut labore et dolore magna.</p>
  <div class="rule"></div>
  <div class="icons">
    <div class="icon">
      <svg viewBox="0 0 80 80"><path d="M20 28a24 24 0 0 1 40-6" fill="none" stroke="#fff" stroke-width="8"/><path d="M60 52a24 24 0 0 1-40 6" fill="none" stroke="#fff" stroke-width="8"/><path d="M66 10v18H48z" fill="#fff"/><path d="M14 70V52h18z" fill="#fff"/></svg>
      <div>REVENUE CYCLE<br>MANAGEMENT</div>
    </div>
    <div class="icon">
      <svg viewBox="0 0 80 80"><path d="M22 10h40v56a8 8 0 0 1-8 8H20" fill="none" stroke="#fff" stroke-width="5"/><path d="M12 18a6 6 0 0 1 10-8v54a8 8 0 0 0 8 10" fill="none" stroke="#fff" stroke-width="5"/><path d="M32 42l7 7 13-15" fill="none" stroke="#fff" stroke-width="5"/></svg>
      <div>COMPLIANCE<br>MANAGEMENT</div>
    </div>
    <div class="icon">
      <svg viewBox="0 0 80 80"><circle cx="40" cy="22" r="8" fill="none" stroke="#fff" stroke-width="5"/><path d="M40 6v6M40 32v6M24 22h6M50 22h6" stroke="#fff" stroke-width="5"/><path d="M10 44l12 14 10 16M70 44L58 58 48 74M22 58l10-6M58 58l-10-6" fill="none" stroke="#fff" stroke-width="5"/></svg>
      <div>HEALTHCARE<br>INNOVATION</div>
    </div>
    <div class="icon">
      <svg viewBox="0 0 80 80"><circle cx="40" cy="38" r="22" fill="none" stroke="#fff" stroke-width="8" stroke-dasharray="10 5"/><circle cx="40" cy="30" r="7" fill="#fff"/><path d="M28 50a12 10 0 0 1 24 0z" fill="#fff"/></svg>
      <div>PRACTICE<br>MANAGEMENT</div>
    </div>
  </div>
</section>

<section class="col cards">
  <div class="card">
    <div class="img" role="img" aria-label="Photo of dental instruments on a tray" style="background:linear-gradient(160deg,#eef1f3,#cfd6db 60%,#f6f6f6)"></div>
    <p>I'm a new Text block ready for your content.</p>
    <a class="btn">Read More</a>
  </div>
  <div class="card">
    <div class="img" role="img" aria-label="Photo of surgeons operating under theatre lights" style="background:linear-gradient(160deg,#3a5f86,#1f3550 60%,#6d8db0)"></div>
    <p>I'm a new Text block ready for your content.</p>
    <a class="btn">Read More</a>
  </div>
  <div class="card">
    <div class="img" role="img" aria-label="Photo of diverse doctors reviewing an x-ray" style="background:linear-gradient(160deg,#e8ecf0,#3d6fa0 55%,#f2f2f2)"></div>
    <p>I'm a new Text block ready for your content.</p>
    <a class="btn">Read More</a>
  </div>
</section>

<section class="col lab">
  <div class="split">
    <div class="copy">
      <h3>Lorem Ipsum</h3>
      <p>Lorem ipsum dolor sit amet, consectetur adipiscing elit, sed do eiusmod tempor incididunt ut labore dolore magna lorem.</p>
    </div>
    <div class="photo" role="img" aria-label="Photo of a pipette filling test tubes in a laboratory rack" style="background:linear-gradient(200deg,#f3f5f6,#dfe6e8 40%,#3fa68f 75%,#e9eef0)"></div>
  </div>
</section>

<section class="col ceo">
  <div class="split">
    <div class="photo" role="img" aria-label="Photo of the female chief executive in a white coat" style="background:linear-gradient(180deg,#ece7e1,#f5f2ee 45%,#d8d1c8)"></div>
    <div class="copy">
      <h3>Lorem ipsum</h3>
      <p>Lorem ipsum dolor sit amet, consectetur adipiscing elit, sed do eiusmod tempor incididunt ut labore et dolore magna. Sed ut perspiciatis unde omnis iste.</p>
      <div class="regards">Kind Regards,</div>
      <div class="signature" role="img" aria-label="Handwritten signature of Evan Marlow"></div>
      <div class="title">CEO, COMPANY NAME</div>
    </div>
  </div>
</section>

<footer class="col footer">
  <div class="social">
    <span aria-label="Social link"></span>
    <span aria-label="Social link"></span>
    <span aria-label="Social link"></span>
    <span aria-label="Social link"></span>
  </div>
  <div class="links">Unsubscribe &nbsp;|&nbsp; View Online</div>
</footer>

</body>
</html>
```